Tem & Crewz

I am looking for help designing a concert benefit flyer. I recently designed a ticket for the event. Attached is the font and the back.
The event is being thrown for Tem Duncan Lo'o Lo'o Perez – He is IMAGE 5112 / 5113/5110 ( I have uploaded 3 options – just use the best that you think would work)
We have 7 different artist’s who will be showcased in the event that we would like to incorporate in the flyer
Image 5107 is the main Artist
“ Vipo and the list below is his Crewz”
Image 5101 is “Moani”
Image 5102 is Brent Tadique
Image 5103 is Ikaika Dela
Image 5104 is Tiana Ruvalo
Image 5106 is Nohea Tabor
Image 5109 is “Pilimoe”
I have uploaded an old flyer we created for a smaller event and was wondering if you could help us design this one ?
Please let me know if you can help and I will go into further details?
Corinne Makuda
HALEWAI MANAGEMENT

```html
<!DOCTYPE html>
<html lang="en">
<head>
<meta charset="utf-8">
<title>Tem &amp; Crewz – Benefit Concert</title>
<link href="https://fonts.googleapis.com/css2?family=Cormorant+Garamond:ital,wght@1,600&family=Oswald:wght@500;600&family=Poppins:wght@600;700&display=swap" rel="stylesheet">
<style>
  :root {
    --bg-charcoal: #262626;
    --bg-black: #0d0d0d;
    --accent-yellow: #ffe500;
    --accent-gold: #e0a81c;
    --mark-red: #8b1c1c;
    --text-white: #ffffff;
    --chevron-grey: #8c8c8c;
    --bar-grey: #bdbdbd;
  }
  * { margin: 0; padding: 0; box-sizing: border-box; }
  html, body { width: 848px; height: 1200px; overflow: hidden; background: var(--bg-black); }
  .flyer {
    position: relative; width: 848px; height: 1200px; overflow: hidden;
    background: var(--bg-charcoal);
    font-family: "Poppins", sans-serif; color: var(--text-white);
  }
  .backdrop { position: absolute; inset: 0; }
  .event-title {
    position: absolute; top: 72px; left: 0; width: 900px; text-align: center;
    font-family: "Cormorant Garamond", serif; font-style: italic; font-weight: 600;
    font-size: 62px; letter-spacing: 1px;
  }
  .recipient-photo { position: absolute; left: 74px; top: 168px; width: 386px; height: 522px; }
  .recipient-label {
    position: absolute; left: 120px; top: 203px;
    color: var(--accent-yellow); font-weight: 700; font-size: 26px;
  }
  .concert-heading {
    position: absolute; left: 484px; top: 156px; width: 340px;
    font-family: "Oswald", sans-serif; font-weight: 600; font-size: 28px; line-height: 1.2;
    color: var(--accent-yellow); text-transform: uppercase; letter-spacing: -0.3px;
  }
  .event-highlights {
    position: absolute; left: 484px; top: 262px; width: 272px;
    font-weight: 600; font-size: 15.5px; line-height: 1.45;
  }
  .proceeds-note {
    position: absolute; left: 482px; top: 402px; width: 250px;
    font-family: "Oswald", sans-serif; font-weight: 500; font-size: 21px; line-height: 1.2;
    color: var(--accent-yellow); text-transform: uppercase;
  }
  .chevrons { position: absolute; left: 552px; top: 470px; }
  .equalizer { position: absolute; left: 66px; top: 682px; }
  .artist-row { position: absolute; left: 0; top: 762px; width: 848px; height: 98px; }
  .artist-portrait, .artist-mark {
    position: absolute; top: 0; width: 96px; height: 96px; border-radius: 50%;
    border: 4px solid var(--accent-gold);
  }
  .artist-portrait { background: linear-gradient(160deg, #c99a6c, #6e4a33 70%, #2f241e); }
  .artist-mark {
    background: var(--mark-red);
    display: flex; align-items: center; justify-content: center;
    font-weight: 700; font-size: 15px; color: var(--text-white);
  }
  .artist-names {
    position: absolute; top: 866px; left: 0; width: 848px; text-align: center;
    color: var(--accent-yellow); font-weight: 700; font-size: 19px;
  }
  .organiser {
    position: absolute; top: 897px; left: 0; width: 848px; text-align: center;
    font-weight: 700; font-size: 17px; text-transform: uppercase;
  }
  .divider { position: absolute; top: 934px; left: 0; width: 848px; height: 4px; background: var(--accent-gold); }
  .invite {
    position: absolute; top: 966px; left: 0; width: 848px; text-align: center;
    color: var(--accent-yellow); font-weight: 700; font-size: 23px;
  }
  .event-date {
    position: absolute; top: 1026px; left: 0; width: 848px; text-align: center;
    color: var(--accent-yellow); font-weight: 600; font-size: 24px;
  }
  .venue {
    position: absolute; top: 1058px; left: 0; width: 848px; text-align: center;
    font-weight: 700; font-size: 21px;
  }
  .entry-note {
    position: absolute; top: 1094px; left: 0; width: 848px; text-align: center;
    font-weight: 700; font-size: 16px;
  }
</style>
</head>
<body>
<main class="flyer">
  <svg class="backdrop" width="848" height="1200" viewBox="0 0 848 1200" aria-hidden="true">
    <polygon points="0,800 848,620 848,1200 0,1200" fill="#0d0d0d"/>
    <rect x="0" y="936" width="848" height="264" fill="#0d0d0d"/>
  </svg>

  <h1 class="event-title">Tem &amp; Crewz</h1>

  <svg class="recipient-photo" viewBox="0 0 386 522" preserveAspectRatio="none" role="img" aria-label="Portrait photo of benefit recipient Tem smiling in a flat cap in front of a canyon">
    <defs>
      <linearGradient id="photoTone" x1="0" y1="0" x2="0" y2="1">
        <stop offset="0" stop-color="#6f9fd1"/>
        <stop offset="0.45" stop-color="#8a7a6a"/>
        <stop offset="1" stop-color="#b9b7b2"/>
      </linearGradient>
    </defs>
    <path d="M0,12 L18,4 L34,14 L52,2 L70,10 L92,0 L110,12 L130,4 L150,14 L172,2 L192,10 L214,0 L236,12 L258,4 L280,14 L300,2 L322,10 L344,0 L366,12 L386,4 L386,504 L366,514 L346,502 L324,518 L304,506 L282,520 L260,504 L238,516 L216,502 L194,518 L172,506 L150,520 L128,504 L106,516 L84,502 L62,518 L40,506 L20,520 L0,508 Z" fill="url(#photoTone)"/>
  </svg>
  <p class="recipient-label">Benefit Recipient</p>

  <h2 class="concert-heading">A benefit concert for Tem Duncan Lo'o Lo'o Perez</h2>
  <p class="event-highlights">Live Hawaiian Music, Entertainment by the "Dawn Daisies" and Live Raffle Giveaway!</p>
  <p class="proceeds-note">All ticket sales will go towards Tem's medical expenses</p>

  <svg class="chevrons" width="200" height="250" viewBox="0 0 200 250" aria-hidden="true">
    <polygon points="48,0 82,0 34,125 82,250 48,250 0,125" fill="var(--chevron-grey)"/>
    <polygon points="106,0 140,0 92,125 140,250 106,250 58,125" fill="var(--chevron-grey)"/>
    <polygon points="164,0 198,0 150,125 198,250 164,250 116,125" fill="var(--chevron-grey)"/>
  </svg>

  <svg class="equalizer" width="506" height="72" viewBox="0 0 506 72" aria-hidden="true">
    <g fill="var(--bar-grey)">
      <rect x="0" y="52" width="6" height="18"/><rect x="9" y="44" width="6" height="26"/><rect x="18" y="36" width="6" height="34"/><rect x="27" y="14" width="6" height="56"/><rect x="36" y="30" width="6" height="40"/><rect x="45" y="40" width="6" height="30"/><rect x="54" y="50" width="6" height="20"/>
      <rect x="78" y="48" width="6" height="22"/><rect x="87" y="30" width="6" height="40"/><rect x="96" y="40" width="6" height="30"/><rect x="105" y="22" width="6" height="48"/><rect x="114" y="36" width="6" height="34"/>
      <rect x="138" y="40" width="6" height="30"/><rect x="147" y="20" width="6" height="50"/><rect x="156" y="4" width="6" height="66"/><rect x="165" y="12" width="6" height="58"/><rect x="174" y="30" width="6" height="40"/><rect x="183" y="44" width="6" height="26"/>
      <rect x="206" y="46" width="6" height="24"/><rect x="215" y="34" width="6" height="36"/><rect x="224" y="18" width="6" height="52"/><rect x="233" y="28" width="6" height="42"/><rect x="242" y="10" width="6" height="60"/><rect x="251" y="24" width="6" height="46"/><rect x="260" y="40" width="6" height="30"/><rect x="269" y="50" width="6" height="20"/>
      <rect x="292" y="28" width="6" height="42"/><rect x="301" y="16" width="6" height="54"/><rect x="310" y="34" width="6" height="36"/><rect x="319" y="44" width="6" height="26"/>
      <rect x="344" y="50" width="6" height="20"/><rect x="353" y="38" width="6" height="32"/><rect x="362" y="26" width="6" height="44"/><rect x="371" y="42" width="6" height="28"/>
      <rect x="394" y="20" width="6" height="50"/><rect x="403" y="8" width="6" height="62"/><rect x="412" y="30" width="6" height="40"/><rect x="421" y="46" width="6" height="24"/>
      <rect x="446" y="44" width="6" height="26"/><rect x="455" y="36" width="6" height="34"/><rect x="464" y="52" width="6" height="18"/>
      <rect x="0" y="70" width="500" height="2"/>
    </g>
  </svg>

  <section class="artist-row" aria-label="Featured artists">
    <div class="artist-mark" style="left:66px">MOANI</div>
    <div class="artist-portrait" role="img" aria-label="Photo of artist Tiana" style="left:169px"></div>
    <div class="artist-portrait" role="img" aria-label="Photo of artist Brent" style="left:273px"></div>
    <div class="artist-portrait" role="img" aria-label="Photo of artist Nohea" style="left:377px"></div>
    <div class="artist-portrait" role="img" aria-label="Photo of artist Ikaika Dela" style="left:481px"></div>
    <div class="artist-portrait" role="img" aria-label="Photo of artist Pilimoe" style="left:585px"></div>
    <div class="artist-portrait" role="img" aria-label="Photo of main artist Vipo" style="left:689px"></div>
  </section>
  <p class="artist-names">Moani - Tiana - Brent - Nohea - Ikaika Dela - Pilimoe - Vipo</p>
  <p class="organiser">Event by Halewai Management Group</p>
  <div class="divider"></div>

  <p class="invite">Please Join Us ForDinner &amp; Live Music</p>
  <p class="event-date">March 9th, 2024 from 4pm - 8pm</p>
  <p class="venue">at the Palmcrest Lu'au Pavillion</p>
  <p class="entry-note">Ticketed Entry Only</p>
</main>
</body>
</html>
```